Business card design needed

Hi,
I was hoping to have a business card designed with a background similar to dark coloured concrete texture. I have a photo of the particular concrete that I would like to be used as the background but for some reason it wouldn't let me upload the image. Please email me for the image and I will send to you asap.
I would like the company name to be in a font that is thin, crisp to reflect 'precision'. I am trying to convey that my services are more precise and have more attention to detail than my competitors. I would like this to be represented through the font if possible.
Colours are at your discretion - although we would like it to attract the eye and stand out. We would like the card to be in a modern style.
I was thinking for an image in the background of the card, or on the side of the card wherever is appropriate, half of a ring saw blade or similar.
The company is a concrete cutting and drilling service - we are a 24 hour 7 day service which is unique to the industry. We provide a more detailed service to our customers and this is the backbone of our reputation.
Target Market(s)
Construction industry & general public
Industry/Entity Type
Concrete
Contact Information for Business Card
Ember Ridge Trenching Pty Ltd
Concrete Cutting & Drilling
24 hour 7 day service
Douglas Whitfield
Director
M: 0492 518 307
P: (07) 3196 4052
E: emberridgetrench@mailvista.net
PO Box 816, Tallowood DC QLD 4173

```html
<!DOCTYPE html>
<html lang="en">
<head>
<meta charset="utf-8">
<title>Ember Ridge Trenching – Business Card</title>
<link rel="stylesheet" href="https://fonts.googleapis.com/css2?family=Alfa+Slab+One&family=Didact+Gothic&display=swap">
<style>
  :root {
    --concrete-light: #e9e0c8;
    --concrete-mid: #cdbd98;
    --concrete-dark: #9c8a64;
    --band-green: #12705a;
    --band-green-deep: #0b5545;
    --panel-orange: #e4451d;
    --panel-orange-deep: #c8351a;
    --tile-orange: #b8301a;
    --name-orange: #f2561f;
    --name-shadow: #3e1606;
    --cream: #dcc8a0;
  }
  html, body {
    margin: 0;
    padding: 0;
    width: 1200px;
    height: 695px;
    overflow: hidden;
    background: #ffffff;
  }
  .card {
    position: relative;
    width: 1200px;
    height: 695px;
    overflow: hidden;
  }
  .concrete-texture {
    position: absolute;
    inset: 0;
    background:
      radial-gradient(ellipse 30% 18% at 12% 10%, rgba(156,138,100,0.55), transparent 70%),
      radial-gradient(ellipse 25% 15% at 55% 6%, rgba(156,138,100,0.45), transparent 70%),
      radial-gradient(ellipse 30% 16% at 88% 12%, rgba(156,138,100,0.35), transparent 70%),
      radial-gradient(ellipse 28% 14% at 20% 92%, rgba(156,138,100,0.45), transparent 70%),
      radial-gradient(ellipse 30% 14% at 75% 94%, rgba(156,138,100,0.4), transparent 70%),
      linear-gradient(180deg, var(--concrete-mid), var(--concrete-light) 50%, var(--concrete-mid));
  }
  .contact-band {
    position: absolute;
    left: 0;
    top: 128px;
    width: 867px;
    height: 447px;
    background: linear-gradient(160deg, var(--band-green) 0%, var(--band-green-deep) 100%);
  }
  .brand-panel {
    position: absolute;
    left: 867px;
    top: 128px;
    width: 333px;
    height: 447px;
    background: linear-gradient(160deg, var(--panel-orange) 0%, var(--panel-orange-deep) 100%);
    border-left: 1px solid #3a2a1a;
  }
  .brand-tile {
    position: absolute;
    left: 34px;
    top: 110px;
    width: 267px;
    height: 236px;
    border-radius: 26px;
    background: var(--tile-orange);
    display: flex;
    align-items: center;
    justify-content: center;
  }
  .brand-name {
    margin: 0;
    font-family: "Didact Gothic", sans-serif;
    font-size: 32px;
    line-height: 1.3;
    letter-spacing: 3px;
    text-align: center;
    color: var(--cream);
    text-transform: uppercase;
  }
  .person-name {
    position: absolute;
    left: 64px;
    top: 168px;
    margin: 0;
    font-family: "Alfa Slab One", serif;
    font-weight: 400;
    font-size: 60px;
    line-height: 1;
    letter-spacing: 1px;
    color: var(--name-orange);
    text-shadow: 2px 3px 0 var(--name-shadow);
    text-transform: uppercase;
    white-space: nowrap;
  }
  .person-role {
    position: absolute;
    left: 64px;
    top: 232px;
    margin: 0;
    font-family: Arial, Helvetica, sans-serif;
    font-weight: 700;
    font-size: 43px;
    line-height: 1;
    color: var(--cream);
    text-transform: uppercase;
  }
  .contact-list {
    position: absolute;
    right: 383px;
    top: 344px;
    margin: 0;
    padding: 0;
    list-style: none;
    text-align: right;
    font-family: "Didact Gothic", sans-serif;
    font-size: 38px;
    letter-spacing: 2.5px;
    line-height: 51px;
    color: var(--cream);
    white-space: nowrap;
  }
  .contact-list li { margin: 0; }
</style>
</head>
<body>
  <main class="card">
    <div class="concrete-texture" role="img" aria-label="Weathered light concrete texture background"></div>

    <section class="contact-band"></section>

    <h1 class="person-name">Douglas Whitfield</h1>
    <p class="person-role">Director</p>

    <ul class="contact-list">
      <li class="contact-mobile">0492 518 307</li>
      <li class="contact-phone">(07) 3196 4052</li>
      <li class="contact-email">emberridgetrench@mailvista.net</li>
      <li class="contact-address">PO Box 816, Tallowood DC QLD 4173</li>
    </ul>

    <aside class="brand-panel">
      <div class="brand-tile">
        <p class="brand-name">Ember Ridge<br>Trenching</p>
      </div>
    </aside>
  </main>
</body>
</html>
```